Business Card Design Project

Mabel's Tonics is a natural skincare business and we need a business card designed. The company focuses on natural products and will be launching with body scrubs and bath fizzies and our mission statement is: To deliver high quality natural beauty products at a good value. It's two cards - one design - the only information changing would be name and email address

Target Market(s)

Females ages 20-50

Industry/Entity Type

Business

Requirements
Must have
• Mabel's Tonics

Corinne Halvorsen-Pitt
T: 800-417-9368
E: Corinne@MabelsTonics.example
W: www.MabelsTonics.example

Ulrich Benedetti
T: 800-417-9368
E: Ulrich@MabelsTonics.example
W: www.MabelsTonics.example
Nice to have
• I'd like to use the colors or text found at www.mabelstonics.example but I'm open to suggestions since design isn't set in stone yet. I would also like to have the words .....a little bit of magic somewhere under the company name in a different type of font. I would like a design that feels clean and maybe a retro feel to it - front and back would be nice but not mandatory

```html
<!DOCTYPE html>
<html lang="en">
<head>
<meta charset="utf-8">
<title>Mabel's Tonics – Business Card</title>
<link rel="stylesheet" href="https://fonts.googleapis.com/css2?family=Delius+Swash+Caps&family=Open+Sans:wght@400;600&family=Cinzel&display=swap">
<style>
  :root {
    --page-bg: #d6d6d6;
    --card-white: #fbfbfb;
    --band-white: #f4f4f4;
    --band-edge: #cfcfcf;
    --brand-purple: #7a1f86;
    --ink: #1c1c1c;
    --label-ink: #3a3a3a;
    --glow: #ff7cf5;
    --nebula-deep: #1a0b2e;
    --nebula-mid: #5a1f8c;
    --nebula-bright: #b43cd8;
  }
  * { box-sizing: border-box; margin: 0; padding: 0; }
  html, body { width: 1200px; height: 765px; overflow: hidden; }
  body {
    position: relative;
    background: var(--page-bg);
    font-family: "Open Sans", Arial, sans-serif;
  }
  .card {
    position: absolute;
    top: 302px;
    width: 574px;
    height: 343px;
    border-radius: 40px;
    overflow: hidden;
  }
  .card--front { left: 16px; }
  .card--back { left: 604px; background: var(--card-white); border: 1px solid #e2e2e2; }

  .nebula {
    position: absolute;
    inset: 0;
    background:
      radial-gradient(ellipse at 85% 20%, rgba(230,140,255,.55), transparent 45%),
      radial-gradient(ellipse at 10% 85%, rgba(255,90,200,.45), transparent 40%),
      radial-gradient(ellipse at 45% 15%, var(--nebula-bright), transparent 55%),
      linear-gradient(180deg, var(--nebula-mid) 0%, var(--nebula-deep) 55%, #2b0c35 100%);
  }

  .band {
    position: absolute;
    left: 0;
    right: 0;
    top: 130px;
    height: 81px;
    background: linear-gradient(180deg, #ffffff 0%, var(--band-white) 60%, #e6e6e6 100%);
    border-top: 1px solid var(--band-edge);
    border-bottom: 2px solid #bdbdbd;
    display: flex;
    align-items: center;
  }
  .band--front { justify-content: center; }

  .brand-name {
    font-family: "Open Sans", Arial, sans-serif;
    font-weight: 600;
    color: var(--brand-purple);
    white-space: nowrap;
  }
  .band--front .brand-name { font-size: 44px; }

  .tagline {
    position: absolute;
    top: 218px;
    left: 0;
    right: 0;
    text-align: center;
    font-family: "Delius Swash Caps", cursive;
    font-size: 28px;
    color: #ffffff;
    text-shadow: 0 0 6px var(--glow), 0 0 14px var(--glow);
  }

  .band--back { padding-left: 54px; }
  .holder-name {
    font-family: "Delius Swash Caps", cursive;
    font-size: 29px;
    color: var(--ink);
    white-space: nowrap;
  }
  .band-divider {
    width: 1px;
    height: 54px;
    background: #7a7a7a;
    margin: 0 14px 0 16px;
  }
  .band--back .brand-name { font-size: 23px; }

  .contact-list {
    position: absolute;
    left: 58px;
    top: 222px;
    list-style: none;
  }
  .contact-list li {
    display: flex;
    align-items: center;
    height: 26px;
    font-size: 18px;
    color: var(--ink);
  }
  .contact-icon {
    width: 19px;
    height: 19px;
    margin-right: 12px;
    flex: none;
  }

  .side-label {
    position: absolute;
    top: 686px;
    font-family: "Cinzel", serif;
    font-size: 14px;
    letter-spacing: 3px;
    color: var(--label-ink);
  }
  .side-label--front { left: 66px; }
  .side-label--back { left: 660px; }
</style>
</head>
<body>

  <section class="card card--front">
    <div class="nebula" role="img" aria-label="Purple cosmic nebula with glowing pink bokeh lights"></div>
    <div class="band band--front">
      <span class="brand-name">Mabel's Tonics</span>
    </div>
    <p class="tagline">A little bit of Magic</p>
  </section>

  <section class="card card--back">
    <div class="band band--back">
      <span class="holder-name">Corinne Halvorsen-Pitt</span>
      <span class="band-divider"></span>
      <span class="brand-name">Mabel's Tonics</span>
    </div>
    <ul class="contact-list">
      <li>
        <svg class="contact-icon" viewBox="0 0 20 20" aria-hidden="true">
          <rect width="20" height="20" rx="4" fill="#111"/>
          <path d="M4 8c0-2 3-3 6-3s6 1 6 3v1h-3V8H7v1H4z" fill="#fff"/>
          <rect x="6" y="10" width="8" height="5" rx="1" fill="#fff"/>
        </svg>
        800-417-9368
      </li>
      <li>
        <svg class="contact-icon" viewBox="0 0 20 20" aria-hidden="true">
          <rect width="20" height="20" rx="4" fill="#111"/>
          <rect x="4" y="6" width="12" height="9" fill="#fff"/>
          <path d="M4 6l6 5 6-5" fill="none" stroke="#111" stroke-width="1.4"/>
        </svg>
        Corinne@MabelsTonics.example
      </li>
      <li>
        <svg class="contact-icon" viewBox="0 0 20 20" aria-hidden="true">
          <rect width="20" height="20" rx="4" fill="#111"/>
          <circle cx="10" cy="10" r="6" fill="none" stroke="#fff" stroke-width="1.3"/>
          <ellipse cx="10" cy="10" rx="2.6" ry="6" fill="none" stroke="#fff" stroke-width="1.1"/>
          <path d="M4 10h12M5 7h10M5 13h10" stroke="#fff" stroke-width="1"/>
        </svg>
        www.MabelsTonics.example
      </li>
    </ul>
  </section>

  <span class="side-label side-label--front">FRONT</span>
  <span class="side-label side-label--back">BACK</span>

</body>
</html>
```